Brivora Collective Business Card Design

We need a business card design for Brivora Collective. We are a healthcare recruiting, wellness and education company. We partner with medical facilities to find quality candidates. We also offer free wellness courses.
The final design should communicate an emphasis on recruiting and wellness
The main purpose of the business card is to utilized it for networking events, give to hospitals, executives, VCs surgery centers and clinics. I want it to be sleek, clean, use of our brand colors and professional.

```html
<!DOCTYPE html>
<html lang="en">
<head>
<meta charset="UTF-8">
<title>Brivora Collective Business Card</title>
<link rel="stylesheet" href="https://fonts.googleapis.com/css2?family=Barlow+Semi+Condensed:wght@700&family=Questrial&display=swap">
<style>
  :root {
    --backdrop: #e3e3e3;
    --brand-green: #025a4f;
    --ink-light: #ffffff;
    --card-shadow: rgba(0, 0, 0, 0.25);
  }
  * { margin: 0; padding: 0; box-sizing: border-box; }
  html, body {
    width: 1200px;
    height: 1200px;
    overflow: hidden;
    background: var(--backdrop);
  }
  .canvas {
    position: relative;
    width: 1200px;
    height: 1200px;
  }
  .card {
    position: absolute;
    left: 188px;
    width: 822px;
    height: 508px;
    background: var(--brand-green);
    color: var(--ink-light);
    box-shadow: 6px 8px 10px var(--card-shadow);
    font-family: "Questrial", "Century Gothic", sans-serif;
  }
  .card--front { top: 71px; }
  .card--back { top: 624px; }

  /* Front: brand name in the mark area */
  .front-brand {
    position: absolute;
    left: 88px;
    top: 198px;
    width: 300px;
    text-align: center;
    font-size: 48px;
    line-height: 1.1;
  }

  /* Front: personal details */
  .identity {
    position: absolute;
    right: 54px;
    top: 104px;
    text-align: right;
  }
  .identity__name {
    font-family: "Barlow Semi Condensed", "Arial Narrow", sans-serif;
    font-weight: 700;
    font-size: 38px;
    line-height: 1;
    letter-spacing: 0.2px;
  }
  .identity__role {
    margin-top: 10px;
    font-size: 21px;
  }

  .contact {
    position: absolute;
    right: 52px;
    list-style: none;
    text-align: right;
    font-size: 21px;
  }
  .contact--direct { top: 245px; }
  .contact--address { top: 342px; }
  .contact__item {
    display: flex;
    justify-content: flex-end;
    align-items: flex-start;
    gap: 14px;
    line-height: 33px;
  }
  .contact__icon {
    width: 15px;
    height: 15px;
    margin-top: 9px;
    flex: none;
    fill: var(--ink-light);
  }
  .contact__address-lines { line-height: 33px; }

  /* Back: centred brand name */
  .back-brand {
    position: absolute;
    left: 0;
    right: 0;
    top: 142px;
    text-align: center;
  }
  .back-brand__square {
    display: block;
    width: 70px;
    height: 70px;
    margin: 0 auto 58px;
    background: var(--ink-light);
  }
  .back-brand__name {
    font-size: 82px;
    line-height: 0.95;
  }
  .back-brand__sub {
    font-size: 44px;
    line-height: 1;
  }
</style>
</head>
<body>
<main class="canvas">
  <section class="card card--front" aria-label="Card front">
    <div class="front-brand">Brivora<br>Collective</div>

    <div class="identity">
      <h1 class="identity__name">YOUR NAME</h1>
      <p class="identity__role">Designation</p>
    </div>

    <ul class="contact contact--direct">
      <li class="contact__item">
        <span>555-014-0192</span>
        <svg class="contact__icon" viewBox="0 0 16 16" aria-hidden="true">
          <path d="M3.6 1.2 5.6 1l1.3 3.2-1.6 1.3a8.6 8.6 0 0 0 5.2 5.2l1.3-1.6 3.2 1.3-.2 2c-.1.7-.7 1.2-1.4 1.2C6.6 13.6 2.4 9.4 2.4 2.6c0-.7.5-1.3 1.2-1.4Z"/>
        </svg>
      </li>
      <li class="contact__item">
        <span>mailid@brivoramail.com</span>
        <svg class="contact__icon" viewBox="0 0 16 16" aria-hidden="true">
          <path d="M1.5 3h13c.3 0 .5.2.5.5v.6L8 8.5 1 4.1v-.6c0-.3.2-.5.5-.5Zm-.5 2.7 7 4.4 7-4.4v6.8c0 .3-.2.5-.5.5h-13a.5.5 0 0 1-.5-.5V5.7Z"/>
        </svg>
      </li>
    </ul>

    <ul class="contact contact--address">
      <li class="contact__item">
        <span class="contact__address-lines">000 N Harbor Lane Suite 00<br>Coral Bay, FL 33000</span>
        <svg class="contact__icon" viewBox="0 0 16 16" aria-hidden="true">
          <path d="M8 0.5a5 5 0 0 1 5 5c0 3.6-5 10-5 10s-5-6.4-5-10a5 5 0 0 1 5-5Zm0 3a2 2 0 1 0 0 4 2 2 0 0 0 0-4Z"/>
        </svg>
      </li>
    </ul>
  </section>

  <section class="card card--back" aria-label="Card back">
    <div class="back-brand">
      <span class="back-brand__square" aria-hidden="true"></span>
      <p class="back-brand__name">Brivora</p>
      <p class="back-brand__sub">collective</p>
    </div>
  </section>
</main>
</body>
</html>
```